Branded Postcard Design for Physician Gift

We’re looking for a clean, professional, and slightly playful postcard design to include inside branded Brevard tumblers being sent to physicians participating in a clinical pilot study.

The card should incorporate our KOR LUMEN TX logo and brand colors (magenta and navy — logo attached), and prominently feature the quote:

“Here’s to staying hydrated as we sprint to the finish line!”

We’d love a design that feels modern and clean — appropriate for a physician audience — with a subtle nod to hydration and the idea of approaching the study’s finish line (e.g., a small water droplet, a minimalist finish line/checkered flag, etc.).

Specs:

Size: Standard postcard (horizontal or vertical layout is fine)

Front: Main quote with design elements

Back: Optional space for a short thank-you message (can be left blank or designed with placeholder text)

Tone:
Professional but friendly, clean and visually appealing with minimal clutter.

I am totally open to your creative ideas - you do not need to follow this description exactly! I'd love to see your ideas. :)

```html
<!DOCTYPE html>
<html lang="en">
<head>
<meta charset="UTF-8">
<title>KOR LUMEN TX Postcard – Front and Back</title>
<link href="https://fonts.googleapis.com/css2?family=Poppins:wght@300;400;500;600;700;800&family=Allura&display=swap" rel="stylesheet">
<style>
  :root {
    --stage: #dedede;
    --magenta: #a5218f;
    --navy: #14213f;
    --ink: #1c1c1c;
    --sky-top: #cfe6fb;
    --sky-mid: #e3f1fc;
    --white: #ffffff;
    --drop-blue: #6fb8f2;
    --drop-deep: #2a86e0;
    --lilac: #c9b6ee;
    --violet: #a98ee6;
    --orchid: #d9a6e6;
    --leaf: #9fc0d2;
  }
  * { margin: 0; padding: 0; box-sizing: border-box; }
  html, body {
    width: 1200px; height: 1200px; overflow: hidden;
    background: var(--stage);
    font-family: "Poppins", sans-serif;
  }
  .postcard {
    position: absolute;
    left: 229px;
    width: 750px; height: 500px;
    overflow: hidden;
    box-shadow: 0 10px 28px rgba(0,0,0,0.28);
  }
  /* Front */
  .postcard--front {
    top: 73px;
    background:
      radial-gradient(ellipse at 25% 30%, rgba(255,255,255,0.7), transparent 45%),
      radial-gradient(ellipse at 85% 40%, rgba(255,255,255,0.6), transparent 40%),
      linear-gradient(180deg, var(--sky-top) 0%, var(--sky-mid) 50%, var(--white) 88%);
  }
  .brand-name {
    position: absolute;
    font-weight: 600;
    color: var(--magenta);
    white-space: nowrap;
    letter-spacing: 0.5px;
  }
  .postcard--front .brand-name { left: 60px; top: 66px; font-size: 19px; }
  .mascot-area {
    position: absolute;
    left: 65px; top: 120px; width: 440px; height: 340px;
    border-radius: 50% 50% 46% 46% / 40% 40% 55% 55%;
    background: radial-gradient(ellipse at 45% 45%, var(--drop-blue) 0%, rgba(111,184,242,0.55) 45%, rgba(255,255,255,0) 72%);
  }
  .headline { position: absolute; left: 0; top: 0; }
  .headline__lead {
    position: absolute; left: 229px; top: 54px;
    font-size: 30px; font-weight: 400; letter-spacing: 5px;
    color: var(--ink); white-space: nowrap;
  }
  .headline__big {
    position: absolute;
    font-size: 70px; font-weight: 800; line-height: 1;
    color: var(--magenta); white-space: nowrap; letter-spacing: -0.5px;
  }
  .headline__big--one { left: 227px; top: 88px; }
  .headline__big--two { left: 288px; top: 148px; }
  .headline__sub {
    position: absolute; left: 450px; top: 212px;
    font-size: 22px; font-weight: 400; color: var(--ink); white-space: nowrap;
  }
  .headline__finish {
    position: absolute; left: 443px; top: 236px;
    font-size: 36px; font-weight: 700; color: var(--ink); white-space: nowrap;
    letter-spacing: -0.5px;
  }
  .web-address {
    position: absolute; left: 443px; top: 414px;
    font-size: 14px; letter-spacing: 3.2px; color: var(--ink); white-space: nowrap;
  }
  .web-address strong { font-weight: 700; }

  /* Back */
  .postcard--back {
    top: 615px;
    background:
      radial-gradient(ellipse at 20% 95%, rgba(169,142,230,0.85), transparent 45%),
      radial-gradient(ellipse at 55% 100%, rgba(160,120,225,0.9), transparent 45%),
      radial-gradient(ellipse at 90% 90%, rgba(217,166,230,0.85), transparent 45%),
      linear-gradient(180deg, var(--white) 0%, #f6f1fc 35%, #e6d9f6 60%, var(--lilac) 100%);
  }
  .postcard--back .brand-name {
    left: 0; right: 0; top: 62px; text-align: center; font-size: 42px;
  }
  .floral {
    position: absolute;
    background: linear-gradient(135deg, var(--leaf), var(--violet));
    opacity: 0.55;
    border-radius: 40%;
  }
  .floral--top { left: 515px; top: 0; width: 235px; height: 170px; border-radius: 0 0 0 80%; }
  .floral--bottom { left: 0; top: 394px; width: 130px; height: 106px; border-radius: 0 80% 0 0; }
  .thanks-title {
    position: absolute; left: 0; right: 0; top: 150px;
    text-align: center;
    font-family: "Allura", cursive;
    font-size: 128px; line-height: 1.1; color: var(--ink);
  }
  .thanks-message {
    position: absolute; left: 165px; width: 420px; top: 315px;
    text-align: center; font-size: 15px; line-height: 1.25; color: var(--ink);
  }
</style>
</head>
<body>
  <section class="postcard postcard--front">
    <div class="mascot-area" role="img" aria-label="Cartoon water droplet mascot running through a magenta finish-line ribbon"></div>
    <div class="brand-name">KOR LUMEN TX</div>
    <h1 class="headline">
      <span class="headline__lead">HERE’S TO</span>
      <span class="headline__big headline__big--one">STAYING</span>
      <span class="headline__big headline__big--two">HYDRATED</span>
      <span class="headline__sub">as we sprint to the</span>
      <span class="headline__finish">FINISH LINE!</span>
    </h1>
    <div class="web-address">www.<strong>korlumentx</strong>.com</div>
  </section>

  <section class="postcard postcard--back">
    <div class="floral floral--top" role="img" aria-label="Watercolour sprig of lilac flowers and leaves"></div>
    <div class="floral floral--bottom" role="img" aria-label="Small watercolour sprig of lilac flowers"></div>
    <div class="brand-name">KOR LUMEN TX</div>
    <h2 class="thanks-title">Thank you</h2>
    <p class="thanks-message">It is a long established fact that a reader will be distracted by the readable content of a page when looking at its layout.</p>
  </section>
</body>
</html>
```